San Antonio Texas Based Law Firm Needs Eye Catching Professional website

The Calloway Law Firm, PLLC is in need of a fresh, eye catching website that makes the small firm look and appear as professional, organized and innovative as possible.

The Firm wants to highlight its expertise in three main areas.
Estate Planning, Insurance and Mediation.

It is a small firm - but growing, so I am looking for the website to have the appearance not of a small firm - but more of the appearance of a leading national firm. The firm was built after obtaining extensive experience working in both private practice and at two Meridian 400 companies.

The firm was formed based on strong relationships and reputation in the industries the Firm serves and and in the local communities.

My logo, which was designed by pixel forge is clever and something I want to make prominent and build from.

Industry/Entity Type

Legal

Coding

Coded - Design and coding required

Number of Pages Required

3 page

Colors
ffffff
000000

Requirements
Must have
• Very good quality pictures.
• Very organized.
• Easy to navigate.
• A contact Us Page.
• On the Estate Planning page, a place for an upcoming seminar sign up - where we
• would get potential client information to mail out confirmation.
• A way to have people subscribe to periodic updates.
• Link to The Calloway Law Firm Chatterly
• A way to download vcard.
Should not have
• Any pictures of gavels, pillars or other common pictures related to law. (Too boring)

```html
<!DOCTYPE html>
<html lang="en">
<head>
<meta charset="utf-8">
<title>The Calloway Law Firm, PLLC</title>
<link rel="stylesheet" href="https://fonts.googleapis.com/css2?family=Roboto+Slab:wght@300;400;700&family=Raleway:wght@400;500;700&family=Roboto:wght@400;500&display=swap">
<style>
:root{
  --black:#000000;
  --ink:#111111;
  --charcoal:#1c1c1c;
  --white:#ffffff;
  --grey-bg:#ebebeb;
  --text:#444444;
  --muted:#666666;
  --line:#cfcfcf;
  --bar:#222222;
}
*{box-sizing:border-box;margin:0;padding:0}
html,body{width:1200px;height:2719px;overflow:hidden;background:var(--white)}
body{position:relative;font-family:'Raleway',sans-serif;color:var(--text)}
a{color:inherit;text-decoration:none}

/* header */
.site-header{position:absolute;left:0;top:0;width:1200px;height:130px;background:var(--white)}
.brand-panel{position:absolute;left:0;top:0;width:370px;height:130px}
.brand{position:absolute;left:100px;top:0;width:180px;height:130px;display:flex;flex-direction:column;align-items:center;justify-content:center;gap:10px;color:var(--white);text-align:center}
.brand-square{width:34px;height:34px;border:2px solid var(--white)}
.brand-name{font-family:'Roboto Slab',serif;font-weight:400;font-size:14px;letter-spacing:1px;text-transform:uppercase}
.top-contacts{position:absolute;left:478px;top:18px;display:flex;align-items:center;gap:22px;font-family:'Roboto',sans-serif;font-size:15px;color:var(--ink)}
.top-contacts .item{display:flex;align-items:center;gap:10px}
.icon-dot{width:30px;height:30px;border-radius:50%;background:var(--ink);display:flex;align-items:center;justify-content:center}
.vcard-btn{background:var(--ink);color:var(--white);font-family:'Roboto Slab',serif;font-size:17px;padding:9px 14px;border-radius:3px}
.main-nav{position:absolute;left:388px;top:80px;display:flex;gap:0;font-family:'Roboto Slab',serif;font-weight:300;font-size:16px;color:var(--ink)}
.main-nav a{padding:0 25px;height:50px;line-height:32px;position:relative}
.main-nav a.active{font-weight:400}
.main-nav a.active::after{content:"";position:absolute;left:0;right:0;bottom:0;height:3px;background:var(--ink)}
.main-nav a.active::before{content:"";position:absolute;left:50%;bottom:3px;margin-left:-7px;border:7px solid transparent;border-bottom-color:var(--ink)}
.search-btn{position:absolute;left:1065px;top:79px;width:34px;height:34px;border:2px solid var(--ink);border-radius:50%;display:flex;align-items:center;justify-content:center}

/* hero */
.hero{position:absolute;left:0;top:130px;width:1200px;height:545px;background:linear-gradient(100deg,#3a3d42 0%,#6b6e72 35%,#8d8a86 60%,#5d6a78 100%)}
.hero-title{position:absolute;left:100px;top:164px;width:453px;height:156px;background:rgba(40,40,40,.75);padding:22px 22px}
.hero-title h1{font-family:'Roboto Slab',serif;font-weight:700;font-size:56px;line-height:62px;color:var(--white)}
.hero-title p{font-family:'Roboto Slab',serif;font-weight:400;font-size:43px;line-height:56px;color:var(--white)}
.slider-dots{position:absolute;left:100px;top:364px;display:flex;gap:12px}
.slider-dots span{width:50px;height:5px;border:1px solid var(--white);border-radius:3px}
.slider-dots span.on{background:var(--white)}

/* signup band */
.signup-band{position:absolute;left:0;top:675px;width:1200px;height:217px;background:linear-gradient(180deg,#2b2b2b 0%,#111 55%,#000 100%)}
.signup-mark{position:absolute;left:100px;top:40px;width:72px;height:72px;border:3px solid var(--white)}
.signup-divider{position:absolute;left:208px;top:40px;width:2px;height:90px;background:var(--white)}
.signup-band h2{position:absolute;left:239px;top:32px;font-family:'Roboto Slab',serif;font-weight:400;font-size:28px;color:var(--white)}
.field{position:absolute;top:86px;width:278px;height:46px;border:2px solid var(--white);color:var(--white);font-family:'Roboto',sans-serif;font-size:17px;padding:10px 12px}
.field.name{left:239px}
.field.email{left:531px}
.signup-btn{position:absolute;left:821px;top:86px;width:279px;height:46px;background:linear-gradient(#fff,#d8d8d8);color:var(--ink);font-family:'Roboto',sans-serif;font-weight:500;font-size:17px;text-align:center;line-height:46px;border-radius:2px}

/* welcome */
.welcome-card{position:absolute;left:100px;top:865px;width:1000px;height:359px;background:var(--white);box-shadow:0 4px 10px rgba(0,0,0,.25);border-bottom:4px solid var(--ink);text-align:center;padding-top:22px}
.section-title{font-family:'Roboto Slab',serif;font-weight:300;font-size:34px;color:var(--ink);text-align:center}
.section-title b{font-weight:700}
.title-rule{width:160px;height:2px;background:var(--ink);margin:14px auto 0}
.welcome-card p{width:850px;margin:32px auto 0;font-size:14px;line-height:30px;color:var(--text)}
.btn-row{display:flex;justify-content:center;gap:14px;margin-top:26px}
.btn{display:inline-block;font-family:'Roboto',sans-serif;font-weight:500;font-size:15px;height:44px;line-height:40px;padding:0 20px;border-radius:5px;border:2px solid var(--ink)}
.btn.dark{background:var(--ink);color:var(--white)}
.btn.light{background:var(--white);color:var(--ink)}
.btn.sm{font-size:13px;height:38px;line-height:34px;padding:0 14px}

/* expertise */
.expertise-head{position:absolute;left:0;top:1270px;width:1200px}
.expert-card{position:absolute;top:1376px;width:310px;height:335px;background:var(--white);border:1px solid var(--line);border-bottom:3px solid var(--ink);box-shadow:0 2px 6px rgba(0,0,0,.12);text-align:center;padding-top:30px}
.expert-card.featured{background:linear-gradient(180deg,#2a2a2a,#0a0a0a);color:var(--white)}
.expert-card svg{display:block;margin:0 auto}
.expert-card h3{font-family:'Roboto Slab',serif;font-weight:400;font-size:24px;color:var(--ink);margin-top:26px}
.expert-card.featured h3,.expert-card.featured p{color:var(--white)}
.expert-card p{width:270px;margin:12px auto 0;font-size:12.5px;line-height:23px;color:var(--text)}
.expert-card .btn{margin-top:14px}
.expert-card.featured .btn{background:var(--white);color:var(--ink);border-color:var(--white)}

/* blog */
.blog-section{position:absolute;left:0;top:1768px;width:1200px;height:553px;background:var(--grey-bg)}
.blog-section .section-title{margin-top:28px}
.blog-card{position:absolute;top:128px;width:300px;height:374px;background:var(--white);border-bottom:3px solid var(--ink);text-align:center}
.blog-photo{width:100%;height:185px}
.blog-card h3{font-family:'Roboto Slab',serif;font-weight:400;font-size:19px;color:var(--ink);margin-top:18px}
.blog-card p{width:270px;margin:10px auto 0;font-size:12.5px;line-height:22px;color:var(--text)}
.blog-card .btn{margin-top:12px}

/* footer */
.site-footer{position:absolute;left:0;top:2321px;width:1200px;height:339px;background:var(--black);color:var(--white)}
.footer-brand{position:absolute;left:100px;top:95px;width:290px;display:flex;flex-direction:column;align-items:center;gap:16px}
.footer-brand .brand-square{width:60px;height:60px;border:3px solid var(--white)}
.footer-brand span{font-family:'Roboto Slab',serif;font-size:19px;letter-spacing:1.5px;text-transform:uppercase}
.footer-col h4{font-family:'Raleway',sans-serif;font-weight:700;font-size:17px;letter-spacing:1px;padding-bottom:10px;border-bottom:2px solid var(--white);display:inline-block}
.footer-col{position:absolute;top:50px}
.quick-links{left:432px}
.quick-links ul{list-style:none;margin-top:22px}
.quick-links li{font-size:14px;line-height:32px}
.contact-col{left:600px;width:230px}
.contact-row{display:flex;gap:16px;margin-top:22px}
.contact-row .ring{flex:none;width:38px;height:38px;border:2px solid var(--white);border-radius:50%;display:flex;align-items:center;justify-content:center}
.contact-row strong{font-size:14px;font-weight:700;display:block;margin-bottom:4px}
.contact-row span{font-size:13px;line-height:20px}
.form-col{left:847px;width:253px}
.f-input{border:1px solid var(--white);font-size:11px;padding:6px 8px;color:var(--white)}
.f-row{display:flex;gap:10px;margin-top:22px}
.f-row .f-input{width:122px;height:36px}
.f-msg{margin-top:8px;height:66px;width:253px}
.f-send{margin-top:16px;display:inline-block;border:1px solid var(--white);font-size:12px;padding:10px 14px;font-family:'Roboto',sans-serif}
.bottom-bar{position:absolute;left:0;top:2660px;width:1200px;height:59px;background:var(--bar);color:var(--white);font-size:14px}
.bottom-bar .copy{position:absolute;left:100px;top:20px}
.social{position:absolute;left:948px;top:12px;display:flex;gap:10px}
.social span{width:34px;height:34px;border:2px solid var(--white);border-radius:50%}
</style>
</head>
<body>

<header class="site-header">
  <svg class="brand-panel" width="370" height="130" viewBox="0 0 370 130" aria-hidden="true"><polygon points="0,0 370,0 310,130 0,130" fill="#000"/></svg>
  <a class="brand" href="#">
    <span class="brand-square"></span>
    <span class="brand-name">The Calloway Law Firm</span>
  </a>
  <div class="top-contacts">
    <span class="item"><span class="icon-dot"><svg width="14" height="10" viewBox="0 0 14 10"><rect x="0.5" y="0.5" width="13" height="9" fill="none" stroke="#fff"/><path d="M0.5 0.5 L7 5.5 L13.5 0.5" fill="none" stroke="#fff"/></svg></span>hello@callowaylegal.com</span>
    <span class="item"><span class="icon-dot"><svg width="14" height="14" viewBox="0 0 14 14"><path d="M3 1 L5 1 L6 4 L4.5 5.5 Q6 8.5 8.5 9.5 L10 8 L13 9 L13 11 Q12 13 10 13 Q2 11 1 3 Q1 1 3 1Z" fill="#fff"/></svg></span>1800 4417 2290</span>
    <a class="vcard-btn" href="#">Download Our VCard</a>
  </div>
  <nav class="main-nav">
    <a class="active" href="#">HOME</a>
    <a href="#">ABOUT US</a>
    <a href="#">ESTATE PLANNING</a>
    <a href="#">SEMINAR</a>
    <a href="#">CONTACT</a>
  </nav>
  <span class="search-btn"><svg width="14" height="14" viewBox="0 0 14 14"><circle cx="6" cy="6" r="4.5" fill="none" stroke="#111" stroke-width="1.8"/><line x1="9.3" y1="9.3" x2="13" y2="13" stroke="#111" stroke-width="1.8"/></svg></span>
</header>

<section class="hero" role="img" aria-label="Photo of smiling clients reviewing documents with an attorney at a desk">
  <div class="hero-title">
    <h1>The Calloway</h1>
    <p>Law Firm</p>
  </div>
  <div class="slider-dots"><span class="on"></span><span></span><span></span></div>
</section>

<section class="signup-band">
  <span class="signup-mark"></span>
  <span class="signup-divider"></span>
  <h2>Signup for Seminar Updates:</h2>
  <div class="field name">Name</div>
  <div class="field email">Email</div>
  <a class="signup-btn" href="#">SIGN UP WITH US</a>
</section>

<section class="welcome-card">
  <h2 class="section-title"><b>Welcome To</b> Calloway Law Firm</h2>
  <div class="title-rule"></div>
  <p>Nemo enim ipsam voluptatem quia voluptas sit aspernatur aut odit aut fugit, sed quia consequuntur magni dolores eos qui ratione voluptatem sequi nesciunt. Neque porro quisquam est, qui dolorem ipsum quia dolor sit amet, consectetur, adipisci velit, sed quia non numquam eius modi tempora incidunt ut labore et dolore magnam aliquam quaerat voluptatem. Ut enim ad minima veniam, quis nostrum exercitationem ullam corporis suscipit laboriosam, nisi ut aliquid ex ea commodi consequatur. Quis autem vel eum iure reprehenderit qui in ea voluptate velit esse quam nihil molestiae consequatur.</p>
  <div class="btn-row"><a class="btn dark" href="#">Read More</a><a class="btn light" href="#">Contact Us</a></div>
</section>

<div class="expertise-head">
  <h2 class="section-title"><b>Our</b> Expertise Areas</h2>
  <div class="title-rule"></div>
</div>

<article class="expert-card" style="left:100px">
  <svg width="110" height="96" viewBox="0 0 110 96" aria-hidden="true">
    <path d="M8 44 L46 10 L84 44" fill="none" stroke="#111" stroke-width="7" stroke-linejoin="round"/>
    <rect x="64" y="14" width="9" height="18" fill="#111"/>
    <path d="M18 42 V86 H62" fill="none" stroke="#111" stroke-width="7"/>
    <rect x="36" y="56" width="18" height="30" fill="#111"/>
    <path d="M82 50 L102 56 V72 Q102 86 82 94 Q62 86 62 72 V56Z" fill="#fff" stroke="#111" stroke-width="4"/>
    <path d="M72 71 L80 79 L93 64" fill="none" stroke="#111" stroke-width="4"/>
  </svg>
  <h3>Estate Planning</h3>
  <p>Nemo enim ipsam voluptatem quia voluptas sit aspernatur aut odit aut fugit sed quia consequ ntur magni dolores.</p>
  <a class="btn dark sm" href="#">Read More</a>
</article>

<article class="expert-card featured" style="left:444px">
  <svg width="100" height="96" viewBox="0 0 100 96" aria-hidden="true">
    <path d="M50 4 L82 14 V40 Q82 60 50 72 Q18 60 18 40 V14Z" fill="none" stroke="#fff" stroke-width="5"/>
    <path d="M36 36 L46 46 L64 26" fill="none" stroke="#fff" stroke-width="5"/>
    <circle cx="20" cy="70" r="7" fill="#fff"/><path d="M6 94 Q6 80 20 80 Q34 80 34 94Z" fill="#fff"/>
    <circle cx="50" cy="72" r="8" fill="#fff"/><path d="M34 96 Q34 82 50 82 Q66 82 66 96Z" fill="#fff"/>
    <circle cx="80" cy="70" r="7" fill="#fff"/><path d="M66 94 Q66 80 80 80 Q94 80 94 94Z" fill="#fff"/>
  </svg>
  <h3>Insurance</h3>
  <p>Nemo enim ipsam voluptatem quia voluptas sit aspernatur aut odit aut fugit sed quia consequ ntur magni dolores.</p>
  <a class="btn light sm" href="#">Read More</a>
</article>

<article class="expert-card" style="left:790px">
  <svg width="110" height="96" viewBox="0 0 110 96" aria-hidden="true">
    <rect x="44" y="8" width="30" height="30" rx="6" fill="#111"/>
    <rect x="74" y="14" width="24" height="18" fill="#111"/>
    <rect x="52" y="38" width="14" height="24" fill="#111"/>
    <rect x="38" y="62" width="42" height="12" fill="#111"/>
    <rect x="26" y="80" width="66" height="8" fill="#111"/>
    <line x1="10" y1="60" x2="26" y2="64" stroke="#111" stroke-width="4"/>
    <line x1="10" y1="76" x2="26" y2="72" stroke="#111" stroke-width="4"/>
    <line x1="96" y1="62" x2="86" y2="66" stroke="#111" stroke-width="4"/>
    <line x1="100" y1="76" x2="88" y2="72" stroke="#111" stroke-width="4"/>
  </svg>
  <h3>Mediation</h3>
  <p>Nemo enim ipsam voluptatem quia voluptas sit aspernatur aut odit aut fugit sed quia consequ ntur magni dolores.</p>
  <a class="btn dark sm" href="#">Read More</a>
</article>

<section class="blog-section">
  <h2 class="section-title"><b>Our</b> Blog Posts</h2>
  <div class="title-rule"></div>

  <article class="blog-card" style="left:100px">
    <div class="blog-photo" role="img" aria-label="Photo of a couple meeting with an advisor over a laptop" style="background:linear-gradient(120deg,#c9b8a6,#8e7d70 55%,#d4cfc8)"></div>
    <h3>Nemo Enim Ipsam Volupta</h3>
    <p>Voluptatem quia voluptas sit aspernatur aut odit aut fugit, sed quia consequuntur magni dolores eos qui ratione voluptatem.</p>
    <a class="btn dark sm" href="#">Read More</a>
  </article>

  <article class="blog-card" style="left:450px">
    <div class="blog-photo" role="img" aria-label="Photo of professionals seated around a meeting table" style="background:linear-gradient(120deg,#dfe6ec,#7f8d99 50%,#2c3440)"></div>
    <h3>Sedut Perspiciatis Omnis</h3>
    <p>Voluptatem quia voluptas sit aspernatur aut odit aut fugit, sed quia consequuntur magni dolores eos qui ratione voluptatem.</p>
    <a class="btn light sm" href="#">Read More</a>
  </article>

  <article class="blog-card" style="left:800px">
    <div class="blog-photo" role="img" aria-label="Photo of a family on a sofa talking with an advisor" style="background:linear-gradient(120deg,#d8cbb8,#9aa6b4 50%,#c7b59c)"></div>
    <h3>Totam Remen Aperiamt</h3>
    <p>Voluptatem quia voluptas sit aspernatur aut odit aut fugit, sed quia consequuntur magni dolores eos qui ratione voluptatem.</p>
    <a class="btn light sm" href="#">Read More</a>
  </article>
</section>

<footer class="site-footer">
  <div class="footer-brand">
    <span class="brand-square"></span>
    <span>The Calloway Law Firm</span>
  </div>

  <div class="footer-col quick-links">
    <h4>QUICK LINKS</h4>
    <ul>
      <li>&gt; Home</li>
      <li>&gt; About Us</li>
      <li>&gt; Estate Planning</li>
      <li>&gt; Seminar</li>
      <li>&gt; Blog</li>
      <li>&gt; Contact Us</li>
    </ul>
  </div>

  <div class="footer-col contact-col">
    <h4>CONTACT US</h4>
    <div class="contact-row">
      <span class="ring"><svg width="12" height="16" viewBox="0 0 12 16"><path d="M6 15 Q0 8 0 6 A6 6 0 0 1 12 6 Q12 8 6 15Z" fill="#fff"/><circle cx="6" cy="6" r="2" fill="#000"/></svg></span>
      <div><strong>CALLOWAY LAW FIRM,</strong><span>218 Alder Crest Ave.<br>San Antonio, TX 78205</span></div>
    </div>
    <div class="contact-row">
      <span class="ring"><svg width="10" height="16" viewBox="0 0 10 16"><rect x="1" y="1" width="8" height="14" rx="1.5" fill="none" stroke="#fff" stroke-width="1.6"/><circle cx="5" cy="12.5" r="1" fill="#fff"/></svg></span>
      <div><strong>PHONE:</strong><span>1800 4417 2290</span></div>
    </div>
    <div class="contact-row">
      <span class="ring"><svg width="14" height="10" viewBox="0 0 14 10"><rect x="0" y="0" width="14" height="10" fill="#fff"/><path d="M0 0 L7 5.5 L14 0" fill="none" stroke="#000"/></svg></span>
      <div><strong>Mail:</strong><span>hello@callowaylegal.com</span></div>
    </div>
  </div>

  <div class="footer-col form-col">
    <h4>CONTACT FORM</h4>
    <div class="f-row"><div class="f-input">Name</div><div class="f-input">Phone</div></div>
    <div class="f-input f-msg">Message</div>
    <span class="f-send">SEND MESSAGE</span>
  </div>
</footer>

<div class="bottom-bar">
  <span class="copy">Copyright © 2016 Calloway Law Firm. All Right Reserved</span>
  <div class="social">
    <span aria-label="Chatterly"></span>
    <span aria-label="Pinwell"></span>
    <span aria-label="Chirpline"></span>
    <span aria-label="Circlepost"></span>
  </div>
</div>

</body>
</html>
```